Bref créative |
Harbourlea Dental Clinic | ||
business cards, letterhead and envelopes design | ||
Use same font as used in my logo | ||
Cutting-Edge Corporate Traditional Modern Professional Simple Bright & Fun-filled |
Dr. Kelsi Tomberg Ravinder | ||
Corrow Arcade - Shop 4.3C, 27 Fenwick Lane, Meadowbank, NSW 2114 |
kelsi@HarbourleaDentalClinic.com.au | ||
www.HarbourleaDentalClinic.com.au | ||
For Business Cards Please include: After-hours Emergency Service: Phone: 02 5173 6648 Mobile: 04 7825 1943 For Envelops Please include: Logo If not delivered please return to Corrow Arcade - Shop 4.3C, 27 Fenwick Lane, Meadowbank, NSW 2114 |
Appointment: For - Date - Time - If you are unable to keep your appointment, please contact us as soon as possible. |

```html
<!DOCTYPE html>
<html lang="en">
<head>
<meta charset="utf-8">
<title>Harbourlea Dental Clinic – Stationery</title>
<link href="https://fonts.googleapis.com/css2?family=Open+Sans:wght@400;600;700&display=swap" rel="stylesheet">
<style>
:root{
  --bg:#8c4b1e;
  --paper:#ffffff;
  --blue:#1a6fb5;
  --blue-dark:#0f4f8c;
  --blue-light:#5fb0e6;
  --ink:#3a3a3a;
  --muted:#8a8f96;
  --faint:#eef2f6;
}
*{margin:0;padding:0;box-sizing:border-box}
html,body{width:1200px;height:470px;overflow:hidden}
body{background:var(--bg);font-family:"Open Sans",Arial,sans-serif;color:var(--ink);position:relative}
.sheet{position:absolute;background:var(--paper);box-shadow:0 3px 8px rgba(0,0,0,.35);overflow:hidden}
.brand{position:absolute;display:flex;align-items:center;gap:4px;color:var(--blue);font-weight:600;white-space:nowrap}
.brand .dot{border-radius:50%;background:var(--blue);flex:none}
.wave{position:absolute;left:0;width:100%}
.watermark{position:absolute;border-radius:50%;background:var(--faint)}

/* envelope */
.envelope-front{left:48px;top:96px;width:326px;height:136px}
.envelope-front .brand{left:14px;top:12px;font-size:9px}
.envelope-front .brand .dot{width:10px;height:10px}
.envelope-back{left:48px;top:236px;width:326px;height:128px}

/* letterhead */
.letterhead{left:388px;top:29px;width:212px;height:410px}
.letterhead .brand{left:18px;top:18px;font-size:9px}
.letterhead .brand .dot{width:10px;height:10px}
.letterhead .watermark{left:66px;top:150px;width:80px;height:80px}
.letterhead .footer{position:absolute;left:6px;right:6px;bottom:12px;text-align:center;font-size:4.6px;line-height:1.55;color:var(--muted)}

/* fax */
.fax{left:618px;top:29px;width:210px;height:410px}
.fax .brand{left:12px;top:14px;font-size:7px}
.fax .brand .dot{width:8px;height:8px}
.fax .address{position:absolute;right:8px;top:10px;width:78px;font-size:3.8px;line-height:1.45;color:var(--muted)}
.fax .title{position:absolute;left:0;right:0;top:70px;text-align:center;font-weight:700;font-size:9px;letter-spacing:.4px}
.fax table{position:absolute;left:28px;top:86px;width:154px;border-collapse:collapse;font-size:3.8px;font-weight:700}
.fax td{border:1px solid #555;height:11px;padding:0 2px;width:25%}
.fax .checks{position:absolute;left:10px;top:176px;right:8px;display:flex;justify-content:space-between;font-size:3.4px;font-weight:700;white-space:nowrap}
.fax .checks span::before{content:"";display:inline-block;width:5px;height:5px;border:1px solid #555;margin-right:2px;vertical-align:middle}
.fax .watermark{left:70px;top:240px;width:70px;height:70px}

/* cards */
.card{width:144px;height:70px}
.card-front{top:96px}
.card-back{top:172px}
.col-a{left:900px}
.col-b{left:1052px}
.card-front .brand{left:8px;top:10px;font-size:6.5px}
.card-front .brand .dot{width:7px;height:7px}
.card-back .name{position:absolute;left:8px;top:8px;font-size:5.5px;font-weight:700;color:var(--blue-dark)}
.card-back .role{position:absolute;left:8px;top:16px;font-size:4px;color:var(--muted)}
.card-back .details{position:absolute;left:8px;top:27px;font-size:3.8px;line-height:1.45;color:var(--ink)}
</style>
</head>
<body>

<div class="sheet envelope-front">
  <div class="brand"><span class="dot"></span>Harbourlea Dental Clinic</div>
  <svg class="wave" style="bottom:0;height:52px" viewBox="0 0 326 52" preserveAspectRatio="none">
    <path d="M0 34 Q165 8 326 24 L326 52 L0 52Z" fill="var(--blue)"/>
    <path d="M0 30 Q165 2 326 18" stroke="var(--blue-light)" stroke-width="1.5" fill="none"/>
  </svg>
</div>

<div class="sheet envelope-back">
  <svg class="wave" style="top:0;height:128px" viewBox="0 0 326 128" preserveAspectRatio="none">
    <path d="M0 0 L326 0 L326 50 Q240 76 163 94 Q86 76 0 50Z" fill="var(--blue)"/>
    <path d="M0 50 Q86 76 163 94 Q240 76 326 50" stroke="var(--blue-light)" stroke-width="2" fill="none"/>
    <path d="M0 0 L326 0 L326 14 Q163 32 0 14Z" fill="var(--blue-dark)"/>
  </svg>
</div>

<div class="sheet letterhead">
  <div class="brand"><span class="dot"></span>Harbourlea Dental Clinic</div>
  <svg class="wave" style="top:40px;height:32px" viewBox="0 0 212 32" preserveAspectRatio="none">
    <path d="M0 12 Q100 30 212 6 L212 18 Q100 40 0 22Z" fill="var(--blue)"/>
    <path d="M0 8 Q100 26 212 3" stroke="var(--blue-light)" stroke-width="1.5" fill="none"/>
  </svg>
  <div class="watermark"></div>
  <div class="footer">
    Corrow Arcade - Shop 4.3C, 27 Fenwick Lane, Kestrel Vale, NSW 2987<br>
    Phone: 02 5173 6648 &nbsp; Mobile: 04 7825 1943 &nbsp; kelsi@HarbourleaDentalClinic.com.au<br>
    www.HarbourleaDentalClinic.com.au
  </div>
</div>

<div class="sheet fax">
  <div class="brand"><span class="dot"></span>Harbourlea Dental Clinic</div>
  <div class="address">Corrow Arcade - Shop 4.3C, 27 Fenwick Lane, Kestrel Vale, NSW 2987<br>Phone: 02 5173 6648<br>Mobile: 04 7825 1943<br>kelsi@HarbourleaDentalClinic.com.au</div>
  <div class="title">FAX COVER</div>
  <table>
    <tr><td>TO:</td><td></td><td>FROM:</td><td></td></tr>
    <tr><td>COMPANY:</td><td></td><td>DATE:</td><td></td></tr>
    <tr><td>FAX:</td><td></td><td>PAGES:</td><td></td></tr>
    <tr><td>PHONE:</td><td></td><td>REFERENCE:</td><td></td></tr>
    <tr><td>CC:</td><td colspan="3"></td></tr>
  </table>
  <div class="checks"><span>URGENT</span><span>FOR REVIEW</span><span>PLEASE COMMENT</span><span>PLEASE REPLY</span><span>PLEASE RECYCLE</span></div>
  <div class="watermark"></div>
</div>

<div class="sheet card card-front col-a">
  <div class="brand"><span class="dot"></span>Harbourlea Dental Clinic</div>
  <svg class="wave" style="bottom:0;height:24px" viewBox="0 0 144 24" preserveAspectRatio="none">
    <path d="M0 14 Q72 2 144 10 L144 24 L0 24Z" fill="var(--blue)"/>
    <path d="M0 12 Q72 0 144 7" stroke="var(--blue-light)" stroke-width="1" fill="none"/>
  </svg>
</div>
<div class="sheet card card-front col-b">
  <div class="brand"><span class="dot"></span>Harbourlea Dental Clinic</div>
  <svg class="wave" style="bottom:0;height:24px" viewBox="0 0 144 24" preserveAspectRatio="none">
    <path d="M0 14 Q72 2 144 10 L144 24 L0 24Z" fill="var(--blue)"/>
    <path d="M0 12 Q72 0 144 7" stroke="var(--blue-light)" stroke-width="1" fill="none"/>
  </svg>
</div>

<div class="sheet card card-back col-a">
  <div class="name">Dr. Kelsi Tomberg Ravinder</div>
  <div class="role">General Dentist</div>
  <div class="details">Phone: 02 5173 6648 &nbsp; Mobile: 04 7825 1943<br>kelsi@HarbourleaDentalClinic.com.au<br>www.HarbourleaDentalClinic.com.au<br>After-hours Emergency Service</div>
</div>
<div class="sheet card card-back col-b">
  <div class="name">Appointment</div>
  <div class="role">For / Date / Time</div>
  <div class="details">If you are unable to keep your appointment,<br>please contact us as soon as possible.<br>Corrow Arcade - Shop 4.3C, 27 Fenwick Lane,<br>Kestrel Vale, NSW 2987</div>
</div>

</body>
</html>
```